New Zealand Export company needs business cards

We need new business cards to match our new logo for a company based in New Zealand who deal specifically with the Pacific Islands. We source, consolidate and ship products out of New Zealand to the Pacific Islands. Will attach our old ones and also new logo.
Would like the Islands we deal with and the areas of work we have access to, to be included on the business cards.

Contact Information for Business Card

T +64 9 571 3048
F +64 9 571 6285
12-18 Kowhai Lane, Drury, 2113
PO Box 814, Drury, Auckland 2247, New Zealand
www.falconfreight.example.nz
E sales@falconfreight.example.nz

Font styles to use
Sans Serif

Colors
85abd2
33a6d7
ffffff

Requirements
Must have
• A company of PWM

```html
<!DOCTYPE html>
<html lang="en">
<head>
<meta charset="utf-8">
<title>Falcon Freight – Business Card</title>
<link rel="stylesheet" href="https://fonts.googleapis.com/css2?family=Montserrat:wght@400;500;700;800&display=swap">
<style>
  :root {
    --page-bg: #e9ebee;
    --card-white: #ffffff;
    --card-black: #1d1e20;
    --brand-navy: #1f5aa8;
    --brand-blue: #2f6fc0;
    --brand-sky: #33a6d7;
    --brand-soft: #85abd2;
    --pattern-light: #eef4fa;
    --pattern-dark: #26282b;
  }
  * { box-sizing: border-box; margin: 0; padding: 0; }
  html, body {
    width: 1200px; height: 1000px; overflow: hidden;
    background: var(--page-bg);
    font-family: "Montserrat", sans-serif;
  }
  .stage {
    position: relative; width: 1200px; height: 1000px;
    display: flex; justify-content: center; align-items: center; gap: 70px;
  }
  .card {
    position: relative; width: 380px; height: 640px;
    border-radius: 26px; overflow: hidden;
    box-shadow: 0 18px 40px rgba(0,0,0,0.18);
  }
  .card-front { background: var(--card-white); }
  .card-back { background: var(--card-black); }
  .card-pattern {
    position: absolute; inset: 0;
  }
  .card-front .card-pattern {
    background: linear-gradient(180deg, var(--pattern-light) 0%, #f7fafd 60%, var(--card-white) 100%);
  }
  .card-back .card-pattern {
    background: linear-gradient(160deg, var(--pattern-dark) 0%, var(--card-black) 100%);
  }
  .front-content {
    position: relative; height: 100%;
    display: flex; flex-direction: column; align-items: center;
    text-align: center; color: var(--brand-blue);
  }
  .brand-lockup {
    margin-top: 110px;
    display: flex; align-items: center; gap: 12px;
  }
  .brand-square { width: 26px; height: 26px; background: var(--brand-sky); }
  .brand-name {
    font-weight: 800; font-size: 27px; letter-spacing: 1px;
    color: var(--brand-navy); line-height: 1;
  }
  .person-name {
    margin-top: 140px;
    font-weight: 800; font-size: 21px; letter-spacing: 0.5px;
    color: var(--brand-navy);
  }
  .person-role {
    font-weight: 500; font-size: 15px; color: var(--brand-sky); margin-top: 2px;
  }
  .divider { width: 240px; height: 1px; background: var(--brand-blue); }
  .divider-top { margin-top: 8px; }
  .contact-icons { display: flex; gap: 6px; margin-top: -10px; }
  .contact-icon { width: 20px; height: 20px; }
  .contact-list {
    list-style: none; margin-top: 18px; margin-bottom: 10px;
    font-size: 15px; line-height: 21px; color: var(--brand-blue);
  }
  .address {
    margin-top: 12px; font-style: normal;
    font-size: 15px; line-height: 21px; color: var(--brand-blue);
  }
  .back-mark {
    position: absolute; right: 34px; bottom: 150px;
    display: flex; align-items: center; gap: 6px;
  }
  .back-mark-square { width: 12px; height: 12px; background: var(--brand-sky); }
  .back-mark-name {
    font-weight: 800; font-size: 12px; letter-spacing: 0.5px; color: var(--card-white);
  }
</style>
</head>
<body>
<main class="stage">
  <section class="card card-front">
    <div class="card-pattern" role="img" aria-label="Faint repeating brand pattern across the card face"></div>
    <div class="front-content">
      <div class="brand-lockup">
        <span class="brand-square"></span>
        <span class="brand-name">FALCON FREIGHT</span>
      </div>
      <h1 class="person-name">MARCUS DELANEY</h1>
      <p class="person-role">Fund Manager</p>
      <div class="divider divider-top"></div>
      <div class="contact-icons">
        <svg class="contact-icon" viewBox="0 0 20 20" aria-label="Phone"><circle cx="10" cy="10" r="10" fill="#33a6d7"/><path d="M6.5 5.5l2 .2.6 2.2-1.2.9a6 6 0 0 0 2.8 2.8l.9-1.2 2.2.6.2 2c-4 .5-8-3.5-7.5-7.5z" fill="#fff"/></svg>
        <svg class="contact-icon" viewBox="0 0 20 20" aria-label="Fax"><circle cx="10" cy="10" r="10" fill="#33a6d7"/><rect x="5.5" y="8" width="9" height="6" rx="1" fill="#fff"/><rect x="7" y="5" width="6" height="3" fill="#fff"/></svg>
        <svg class="contact-icon" viewBox="0 0 20 20" aria-label="Email"><circle cx="10" cy="10" r="10" fill="#33a6d7"/><rect x="5" y="6.5" width="10" height="7" fill="#fff"/><path d="M5 6.5l5 4 5-4" fill="none" stroke="#33a6d7" stroke-width="1"/></svg>
        <svg class="contact-icon" viewBox="0 0 20 20" aria-label="Website"><circle cx="10" cy="10" r="10" fill="#33a6d7"/><circle cx="10" cy="10" r="4.8" fill="none" stroke="#fff" stroke-width="1.2"/><path d="M5.2 10h9.6M10 5.2v9.6" stroke="#fff" stroke-width="1"/></svg>
      </div>
      <ul class="contact-list">
        <li>+64 9 571 3048</li>
        <li>+64 9 571 6285</li>
        <li>sales@falconfreight.example.nz</li>
        <li>www.falconfreight.example.nz</li>
      </ul>
      <div class="divider"></div>
      <address class="address">
        12-18 Kowhai Lane, Drury, 2113<br>
        PO Box 814, Drury<br>
        Auckland 2247, New Zealand
      </address>
    </div>
  </section>

  <section class="card card-back">
    <div class="card-pattern" role="img" aria-label="Dark tone-on-tone repeating brand pattern"></div>
    <div class="back-mark">
      <span class="back-mark-square"></span>
      <span class="back-mark-name">FALCON FREIGHT</span>
    </div>
  </section>
</main>
</body>
</html>
```